Need a sleek, professional business card design for a Web Development business

I need a unique business card designed for a web development company. It is also the parent company for any ventures I do, such as my ClipWave channel, startup ideas I have, etc. I am the single member of "Bright Harbor Code LLC." I will attach my basic logo here, so you will see the current color scheme and have the asset available. Thank you!

Target Market(s)

Startups, SMB's, Professionals

Industry/Entity Type

Business

Font styles to use
Other font styles liked:
• Lovello for headings is what I use, but not necessary.

Colors

Designer to choose colors to be used in the design.

Requirements
Nice to have
• Sleek is the word. Professional, modern, dark.
Should not have
• Any work from someone else's design. Lacking originality.

```html
<!DOCTYPE html>
<html lang="en">
<head>
<meta charset="utf-8">
<title>Bright Harbor Code LLC — Business Card</title>
<link href="https://fonts.googleapis.com/css2?family=Bebas+Neue&family=Roboto:wght@300;400&display=swap" rel="stylesheet">
<style>
  :root {
    --page-bg: #ecebe8;
    --card-bg: #ffffff;
    --accent: #e0566a;
    --accent-soft: #ee9aa6;
    --mark-dark: #1d1d1f;
    --text-grey: #6d6d72;
    --text-dark: #3a3a3e;
  }
  * { margin: 0; padding: 0; box-sizing: border-box; }
  html, body { width: 1200px; height: 1023px; overflow: hidden; }
  body {
    background: var(--page-bg);
    display: flex;
    align-items: center;
    justify-content: center;
    font-family: "Roboto", Arial, sans-serif;
  }
  .card {
    position: relative;
    width: 900px;
    height: 520px;
    background: linear-gradient(135deg, #ffffff 0%, #f4f4f4 100%);
    border-radius: 22px;
    box-shadow: 0 18px 40px rgba(0,0,0,0.18);
    overflow: hidden;
  }
  .side-band {
    position: absolute;
    left: 70px;
    top: 0;
    width: 96px;
    height: 100%;
    background: linear-gradient(180deg, var(--accent) 0%, var(--accent) 45%, var(--accent-soft) 100%);
  }
  .brand-mark {
    position: absolute;
    left: 58px;
    top: 70px;
    width: 120px;
    height: 120px;
    background: var(--mark-dark);
    border-radius: 10px;
    display: flex;
    align-items: center;
    justify-content: center;
    text-align: center;
    padding: 10px;
  }
  .brand-mark__name {
    font-family: "Bebas Neue", Arial, sans-serif;
    font-size: 20px;
    line-height: 1.05;
    letter-spacing: 1px;
    color: #ffffff;
  }
  .details {
    position: absolute;
    left: 220px;
    top: 70px;
  }
  .company-name {
    font-family: "Bebas Neue", Arial, sans-serif;
    font-size: 50px;
    letter-spacing: 3px;
    color: var(--accent);
    line-height: 1;
  }
  .person-name {
    margin-top: 58px;
    font-family: "Bebas Neue", Arial, sans-serif;
    font-size: 54px;
    letter-spacing: 3px;
    color: var(--accent);
    line-height: 1;
  }
  .person-title {
    font-size: 21px;
    font-weight: 300;
    color: var(--text-grey);
    margin-top: 4px;
  }
  .address {
    margin-top: 26px;
    font-size: 21px;
    font-weight: 300;
    color: var(--text-grey);
    line-height: 1.3;
  }
  .contacts {
    list-style: none;
    margin-top: 24px;
  }
  .contacts li {
    display: flex;
    align-items: center;
    gap: 14px;
    font-size: 21px;
    font-weight: 300;
    color: var(--text-dark);
    line-height: 1.35;
  }
  .contacts svg { width: 14px; height: 14px; flex: none; }
  .contacts .highlight { color: var(--accent); }
</style>
</head>
<body>
  <div class="card">
    <div class="side-band"></div>
    <div class="brand-mark">
      <span class="brand-mark__name">Bright Harbor Code</span>
    </div>
    <div class="details">
      <h1 class="company-name">Bright Harbor Code LLC.</h1>
      <h2 class="person-name">Marek Lindqvist</h2>
      <p class="person-title">Managing Partner</p>
      <p class="address">Kornweg 12, 69115<br>Heidelberg, Germany</p>
      <ul class="contacts">
        <li>
          <svg viewBox="0 0 16 16" aria-hidden="true"><path d="M4 1.5l2.5 3-1.5 1.8c.9 1.9 2.3 3.3 4.2 4.2l1.8-1.5 3 2.5-1.5 2.5C7.5 13.5 2.5 8.5 1.5 3z" fill="#e0566a"/></svg>
          +49 170 482 106 57
        </li>
        <li>
          <svg viewBox="0 0 16 16" aria-hidden="true"><rect x="1.5" y="3.5" width="13" height="9" rx="1" fill="none" stroke="#e0566a" stroke-width="1.5"/><path d="M2 4l6 5 6-5" fill="none" stroke="#e0566a" stroke-width="1.5"/></svg>
          info@brightharborcode.com
        </li>
        <li>
          <svg viewBox="0 0 16 16" aria-hidden="true"><circle cx="8" cy="8" r="6.5" fill="none" stroke="#e0566a" stroke-width="1.4"/><ellipse cx="8" cy="8" rx="2.8" ry="6.5" fill="none" stroke="#e0566a" stroke-width="1.2"/><path d="M1.5 8h13" stroke="#e0566a" stroke-width="1.2"/></svg>
          <span>www.<span class="highlight">brightharborcode</span>.com</span>
        </li>
      </ul>
    </div>
  </div>
</body>
</html>
```